Carpet Cleaning Door Hanger Design Project

please design a door hanger for us. we do carpet cleaning. our company name is Velta Rug Works. our telephone number is 866-402-5719.

please make a special offer coupon.

please add bullets containing the following info-
Professional carpet, hardwood, tile & grout deep steam cleaning.
kid & pet safe.
fast drying.
100% eco friendly / toxin free products.
pet stain/s & odor control.
same day appointments.
clean uniformed employees.
and please put few other catchy lines.

please make a $20.00 of carpet cleaning coupon (restrictions apply).
please make a rooms starting at $59.99 (restrictions apply).

please also put- when you want the best for less call velta rug works.

Target Market(s)

home owners, home renters. new home buyers. new home sellers.

Industry/Entity Type

Home Improvement

Requirements
Must have
• special offer.
• double sided.
• must be a design for a door hanger.
Nice to have
• 100% satisfaction guaranteed bubble.
Should not have
• no website please

```html
<!DOCTYPE html>
<html lang="en">
<head>
<meta charset="utf-8">
<title>Velta Rug Works – Door Hanger</title>
<link rel="stylesheet" href="https://fonts.googleapis.com/css2?family=Quicksand:wght@500;600&family=Open+Sans:wght@400;600;700&display=swap">
<style>
  :root {
    --navy: #1f4873;
    --navy-deep: #163a60;
    --sky: #2f8fd0;
    --ink: #333a42;
    --grey-coupon: #3b3d40;
    --paper: #ffffff;
    --stage: #e9eaec;
    --photo-front-a: #d8d4cf;
    --photo-front-b: #a9a39b;
    --photo-back-a: #f1eee9;
    --photo-back-b: #c9c3ba;
  }
  * { box-sizing: border-box; margin: 0; padding: 0; }
  html, body { width: 1200px; height: 887px; overflow: hidden; }
  body {
    background: var(--stage);
    font-family: "Open Sans", Arial, sans-serif;
    color: var(--ink);
    position: relative;
  }

  .hanger {
    position: absolute;
    top: 60px;
    width: 315px;
    height: 765px;
    background: var(--paper);
    box-shadow: 0 6px 18px rgba(0,0,0,.18);
    overflow: hidden;
  }
  .hanger--front { left: 215px; }
  .hanger--back { left: 670px; }

  .photo { position: absolute; left: 0; top: 0; width: 100%; }
  .hanger--front .photo { height: 470px; background: linear-gradient(160deg, var(--photo-front-a), var(--photo-front-b)); }
  .hanger--back .photo { height: 320px; background: linear-gradient(160deg, var(--photo-back-a), var(--photo-back-b)); }

  .hole {
    position: absolute;
    width: 112px; height: 112px;
    border-radius: 50%;
    background: var(--stage);
    left: 50%; top: 17px;
    transform: translateX(-50%);
  }

  .wave { position: absolute; left: 0; width: 100%; display: block; }
  .hanger--front .wave { top: 400px; height: 100px; }
  .hanger--back .wave { top: 230px; height: 115px; }

  .brand {
    position: absolute;
    font-family: "Quicksand", "Trebuchet MS", sans-serif;
    font-weight: 600;
    color: var(--navy);
    text-transform: uppercase;
    line-height: .95;
    letter-spacing: -1px;
  }
  .hanger--front .brand {
    top: 505px; width: 100%;
    text-align: center; font-size: 40px;
  }
  .hanger--back .brand {
    top: 300px; right: 17px;
    text-align: left; font-size: 29px;
  }

  .tagline {
    position: absolute; top: 598px; width: 100%;
    text-align: center; color: var(--navy);
    font-size: 23px; line-height: 1.1; text-transform: uppercase;
  }
  .tagline strong { font-weight: 700; }

  .call-line {
    position: absolute; width: 100%;
    text-align: center; text-transform: uppercase;
    font-size: 14px; line-height: 1.05; color: var(--ink);
  }
  .phone-bar {
    position: absolute; left: 50%; transform: translateX(-50%);
    width: 270px; height: 35px; line-height: 35px;
    background: var(--navy);
    border-radius: 9px;
    color: #fff;
    text-align: center;
    font-size: 29px; font-weight: 400;
    box-shadow: inset 0 -3px 0 var(--navy-deep);
  }

  .hanger--front .call-line { top: 664px; }
  .hanger--front .phone-bar { top: 698px; }

  .benefits {
    position: absolute; top: 372px; left: 18px; right: 12px;
    list-style: none; font-size: 13.3px; line-height: 16px;
  }
  .benefits li { display: flex; align-items: flex-start; margin-bottom: 7px; }
  .benefits .pair { gap: 14px; }
  .benefits .pair span { display: flex; }
  .tick { width: 11px; height: 11px; margin: 4px 3px 0 0; flex: none; }

  .hanger--back .call-line { top: 544px; }
  .hanger--back .phone-bar { top: 576px; }

  .cut-line {
    position: absolute; top: 652px; left: 0; width: 100%;
    border-top: 1.5px dotted var(--navy);
  }
  .coupons {
    position: absolute; top: 664px; left: 15px; right: 16px;
    display: flex; justify-content: space-between;
  }
  .coupon {
    height: 73px;
    background: var(--grey-coupon);
    border-radius: 16px 0 16px 0;
    color: #fff; text-align: center;
    display: flex; flex-direction: column; justify-content: center;
    text-transform: uppercase;
  }
  .coupon--cash { width: 116px; }
  .coupon--rooms { width: 138px; }
  .coupon .amount { font-weight: 700; font-size: 29px; line-height: 1; }
  .coupon .label { font-size: 12px; line-height: 1.05; }
  .coupon--rooms .label { font-size: 11px; }
  .coupon--rooms .amount { margin-top: 3px; }
  .restrictions {
    position: absolute; top: 741px; width: 100%;
    text-align: center; color: var(--navy);
    font-size: 12.5px; text-transform: uppercase; font-weight: 600;
  }
</style>
</head>
<body>

<section class="hanger hanger--front" aria-label="Door hanger front">
  <div class="photo" role="img" aria-label="Photo of cleaners vacuuming a white shag rug in a bright living room"></div>
  <div class="hole"></div>
  <svg class="wave" viewBox="0 0 315 100" preserveAspectRatio="none" aria-hidden="true">
    <path d="M0 84 C110 58 210 30 315 38 L315 100 L0 100 Z" fill="#fff"/>
    <path d="M0 46 C100 22 210 2 315 14 L315 18 C210 6 100 26 0 52 Z" fill="var(--sky)"/>
    <path d="M0 52 C100 26 210 6 315 18 L315 40 C210 30 110 58 0 88 Z" fill="var(--navy)"/>
    <path d="M0 95 C110 66 210 42 315 46 L315 50 C210 47 110 71 0 100 Z" fill="var(--navy)"/>
  </svg>
  <h1 class="brand">Velta Rug<br>Works</h1>
  <p class="tagline"><strong>A Cleaner Home</strong> is a<br><strong>Healthier Home</strong></p>
  <p class="call-line">When you want the best for less<br>call velta rug works</p>
  <div class="phone-bar">866-402-5719</div>
</section>

<section class="hanger hanger--back" aria-label="Door hanger back">
  <div class="photo" role="img" aria-label="Photo of a vacuum cleaner on a cream carpet"></div>
  <div class="hole"></div>
  <svg class="wave" viewBox="0 0 315 115" preserveAspectRatio="none" aria-hidden="true">
    <path d="M0 100 C110 76 210 40 315 36 L315 115 L0 115 Z" fill="#fff"/>
    <path d="M0 66 C100 52 200 10 315 6 L315 10 C200 14 100 56 0 72 Z" fill="var(--sky)"/>
    <path d="M0 72 C100 56 200 14 315 10 L315 38 C210 42 110 78 0 104 Z" fill="var(--navy)"/>
  </svg>
  <h2 class="brand">Velta Rug<br>Works</h2>

  <ul class="benefits">
    <li><svg class="tick" viewBox="0 0 12 12"><path d="M1 6 L4.5 10 L11 1" fill="none" stroke="var(--sky)" stroke-width="1.8"/></svg><span>Professional carpet, hardwood, tile &amp; grout deep steam cleaning.</span></li>
    <li class="pair">
      <span><svg class="tick" viewBox="0 0 12 12"><path d="M1 6 L4.5 10 L11 1" fill="none" stroke="var(--sky)" stroke-width="1.8"/></svg>kid &amp; pet safe.</span>
      <span><svg class="tick" viewBox="0 0 12 12"><path d="M1 6 L4.5 10 L11 1" fill="none" stroke="var(--sky)" stroke-width="1.8"/></svg>fast drying</span>
    </li>
    <li><svg class="tick" viewBox="0 0 12 12"><path d="M1 6 L4.5 10 L11 1" fill="none" stroke="var(--sky)" stroke-width="1.8"/></svg><span>100% eco friendly / toxin free products.</span></li>
    <li><svg class="tick" viewBox="0 0 12 12"><path d="M1 6 L4.5 10 L11 1" fill="none" stroke="var(--sky)" stroke-width="1.8"/></svg><span>pet stain/s &amp; odor control</span></li>
    <li><svg class="tick" viewBox="0 0 12 12"><path d="M1 6 L4.5 10 L11 1" fill="none" stroke="var(--sky)" stroke-width="1.8"/></svg><span>same day appointments</span></li>
    <li><svg class="tick" viewBox="0 0 12 12"><path d="M1 6 L4.5 10 L11 1" fill="none" stroke="var(--sky)" stroke-width="1.8"/></svg><span>clean uniformed employees</span></li>
  </ul>

  <p class="call-line">When you want the best for less<br>call velta rug works</p>
  <div class="phone-bar">866-402-5719</div>

  <div class="cut-line"></div>
  <div class="coupons">
    <div class="coupon coupon--cash">
      <span class="amount">$20.00</span>
      <span class="label">Carpet cleaning<br>coupon</span>
    </div>
    <div class="coupon coupon--rooms">
      <span class="label">Please make a<br>rooms starting at</span>
      <span class="amount">$59.99</span>
    </div>
  </div>
  <p class="restrictions">Restrictions apply</p>
</section>

</body>
</html>
```